ASL Learning Website Application Pages Redesign

Introduction:
We need a redesign of the internal pages of our website, SignQuiverly.com. The current website design has been in place for many years and is not mobile friendly. We want an updated design that makes the site look cleaner, more professional, and mobile accessible. We are looking for a design that eliminates the clutter on each page, and makes the site simple and easy to use. We will be interested in your design if it is unique and creative. Don't be afraid to completely change the look of the site.

We need the designs sliced up into clean HTML files that are responsive and work well on both mobile and desktop computers. We will implement the PHP needed to make the pages functional.

About Us:
SignQuiverly is a subscription-based website for American Sign Language (ASL) video lessons. The content is for anyone who wishes to learn ASL, regardless of age. It has been designed to instruct Deaf students, parents of Deaf children, and the community-at-large. All lessons are taught by Deaf experts of ASL.

Overview:
The website before log-in does not need any changes. There are five key pages within the internal website (after log-in) that need to be redesigned; they are listed below. Note that some pages (Dictionary and Activity) have multiple sub-pages, so there are about 6-8 pages in total to design, depending on how you decide to approach this (more info in the pages’ respective instruction documents).

The new page designs should retain their existing features, and as stated before, should be mobile friendly. However, you may combine, collapse, or completely change the look of these features. Each page to redesign has a separate instruction document attachment, and screenshots of the current version of the page. Our logo has also been attached. If you want to see the website pages for yourself, you can also go to our website (SignQuiverly.com) and use a free trial to get access to the internal site.

As for design preferences, we want our site to be modern-looking and mature. We’re looking for an inviting, educational style that can attract both high school students and adults. We’re happy with the current font and color scheme, but we’re always open to ideas!

Additional Notes:
- Every page has the same header and footer. You could keep these the same, or change them, based on your discretion.
- Currently, every page also has a breadcrumb. The breadcrumb is unnecessary and you may remove it. However, the “add/remove from favorites” button on the right of the breadcrumb is necessary to keep somewhere on the page.

Pages:
Here’s a list of the five key pages we need redesigned:
- Dashboard
- Dictionary
- Lesson
- Activity
- All Lessons

Each page has its own instruction document. These are attached separately.

Just purchased a $150 for Top designers. I need to give them time to submit their designs . Can I have 7 more days?

Target Market(s)

Deaf students, parents of Deaf children, and the community-at-large interested in learning ASL

Coding

Number of Pages Required

5+ page

Font styles to use
Sans Serif

Requirements
Must have
• Responsive design - the full application experience should be available on mobile devices.
Follow the directions on the design brief.
Nice to have
• Be creative! Please play around with, or even completely change, the look of the site.

```html
<!DOCTYPE html>
<html lang="en">
<head>
<meta charset="utf-8">
<title>SignQuiverly – Dictionary pages</title>
<link href="https://fonts.googleapis.com/css2?family=Lato:wght@400;700;900&display=swap" rel="stylesheet">
<style>
:root{
  --bg:#e3e3e3;
  --green:#5aa832;
  --green-dark:#4a8f28;
  --cream:#f7f0df;
  --nav:#5d5d5d;
  --ink:#222;
  --text:#555;
  --muted:#8a8a8a;
  --line:#e2e2e2;
  --letter:#7a7a7a;
  --red:#d8322b;
  --blue:#2f8fe0;
  --field:#f1f1f1;
}
*{margin:0;padding:0;box-sizing:border-box}
html,body{width:1200px;height:1172px;overflow:hidden;background:var(--bg)}
body{font-family:'Lato',sans-serif;color:var(--text)}
.stage{position:absolute;left:0;top:0;width:1950px;height:1904px;transform:scale(.61538);transform-origin:0 0}
.page{position:absolute;width:511px;background:#fff;overflow:hidden}
.page--dictionary{left:128px;top:135px;height:1633px}
.page--modal{left:720px;top:135px;height:1633px}
.page--search{left:1311px;top:135px;height:579px}

/* header */
.site-header{position:absolute;left:0;top:0;width:511px;height:51px;background:var(--green)}
.brand{position:absolute;left:0;top:0;width:186px;height:51px;background:var(--cream);display:flex;align-items:center;padding-left:40px;gap:5px}
.brand::after{content:"";position:absolute;right:-8px;top:17px;border-left:8px solid var(--cream);border-top:8px solid transparent;border-bottom:8px solid transparent}
.brand-dot{width:9px;height:9px;border-radius:50%;background:var(--green)}
.brand-name{font-size:15px;font-weight:700;color:#3a3a3a}
.tagline{position:absolute;left:220px;top:10px;color:#fff}
.tagline strong{display:block;font-size:8.2px;font-weight:900;letter-spacing:-.05px}
.tagline span{display:block;font-size:5.6px;margin-top:6px;padding-left:8px}
.tagline em{font-style:italic}
.main-nav{position:absolute;left:0;top:51px;width:511px;height:20px;background:var(--nav);display:flex;align-items:center;padding-left:54px;gap:12.5px}
.main-nav a{color:#fff;font-size:6.3px;font-weight:700;text-decoration:none;white-space:nowrap}
.caret{display:inline-block;margin-left:2px;border-top:2.4px solid #fff;border-left:2px solid transparent;border-right:2px solid transparent;vertical-align:middle}

/* title + search */
.page-title{position:absolute;left:48px;top:91px;font-size:14px;font-weight:700;color:var(--ink)}
.page-sub{position:absolute;left:48px;top:112px;font-size:5.8px;font-weight:700;color:var(--ink)}
.search{position:absolute;left:47px;display:flex;align-items:center;font-size:5.6px;color:var(--ink)}
.search label{width:73px}
.field{height:17px;border-radius:9px;background:var(--field);border:1px solid #ececec;font-size:4.8px;color:#aaa;display:flex;align-items:center;padding-left:8px}
.search .field{width:139px}
.btn{height:17px;border-radius:9px;background:var(--green);color:#fff;font-size:6.2px;font-weight:700;display:flex;align-items:center;justify-content:center;margin-left:4px}
.search .btn{width:48px}

/* alphabet */
.alphabet{position:absolute;left:48px;display:flex;gap:5.6px}
.alphabet span{width:11px;height:11px;background:var(--letter);color:#fff;font-size:6px;font-weight:700;display:flex;align-items:center;justify-content:center}
.alphabet span.is-current{background:var(--green)}

/* word list */
.word-list{position:absolute;top:190px;list-style:none}
.word-list li{height:12.77px;font-size:5.2px;line-height:12.77px;color:#666;white-space:nowrap;padding-left:9px;position:relative}
.word-list li::before{content:"";position:absolute;left:0;top:4.3px;width:4.4px;height:4.4px;border-radius:50%;background:var(--green)}
.col-1{left:48px}.col-2{left:118px}.col-3{left:185px}.col-4{left:254px}.col-5{left:320px}.col-6{left:409px}

/* footer */
.site-footer{position:absolute;left:0;bottom:0;width:511px;height:196px;border-top:2px solid var(--green);background:#fff}
.foot-brand{position:absolute;left:43px;top:24px;display:flex;align-items:center;gap:5px}
.foot-brand .brand-name{font-size:14px}
.foot-about{position:absolute;left:43px;top:61px;width:127px;font-size:5.2px;line-height:11px;color:#666}
.foot-divider{position:absolute;top:26px;width:1px;height:92px;background:var(--line)}
.foot-head{position:absolute;top:17px;font-size:8.6px;font-weight:700;color:var(--ink)}
.foot-links{position:absolute;top:33px;list-style:none;font-size:5px;color:#666}
.foot-links li{height:11px}
.contact{position:absolute;left:355px;top:32px;list-style:none;font-size:5px;color:#666}
.contact li{display:flex;align-items:center;gap:5px;height:17px}
.contact svg{width:6px;height:6px;fill:var(--green)}
.foot-rule{position:absolute;left:43px;top:161px;width:433px;height:1px;background:var(--line)}
.copyright{position:absolute;left:43px;top:175px;font-size:5px;color:#666}
.social{position:absolute;left:389px;top:174px;display:flex;gap:7.5px}
.social span{width:12px;height:12px;border-radius:50%;border:1px solid var(--green)}

/* modal view */
.shade{position:absolute;inset:0;background:rgba(40,40,40,.52)}
.vocab-modal{position:absolute;left:172px;top:185px;width:167px;height:196px;background:#fff;box-shadow:0 2px 8px rgba(0,0,0,.3)}
.modal-bar{height:17px;background:var(--green);display:flex;align-items:center;padding:0 7px;color:#fff;font-size:6.2px;font-weight:700}
.modal-bar .plus{width:6px;height:6px;margin-right:4px}
.modal-bar u{flex:1}
.modal-close{width:7px;height:7px;border-radius:50%;background:#fff;position:relative}
.modal-close::before,.modal-close::after{content:"";position:absolute;left:3px;top:1.3px;width:1px;height:4.4px;background:var(--green);transform:rotate(45deg)}
.modal-close::after{transform:rotate(-45deg)}
.video{position:relative;height:129px;background:linear-gradient(180deg,#3f8f6a,#2d7356);margin:0}
.slow-toggle{position:absolute;right:4px;top:7px;background:#fff;font-size:4.6px;color:#333;padding:2px 4px;display:flex;align-items:center;gap:3px}
.slow-toggle i{width:4px;height:4px;border:.6px solid #555}
.video-controls{position:absolute;left:0;right:0;bottom:5px;height:12px;background:#111;display:flex;align-items:center;padding:0 5px;color:#fff;font-size:4px;gap:5px}
.video-controls b{border-left:3px solid #fff;border-top:2px solid transparent;border-bottom:2px solid transparent}
.video-controls em{flex:1}
.term{position:absolute;left:14px;font-size:5.2px;color:#333}
.term .blue{color:var(--blue)}
.term .red{color:var(--red)}

/* search page */
.results{position:absolute;top:164px;left:0;width:511px;height:10px}
.results span{position:absolute;font-size:5.4px;color:#666;padding-left:9px}
.results span::before{content:"";position:absolute;left:0;top:.7px;width:4.4px;height:4.4px;border-radius:50%;background:var(--green)}
.results .hit{color:var(--red)}
.request-card{position:absolute;left:48px;top:199px;width:414px;height:137px;background:#fff;box-shadow:0 0 6px rgba(0,0,0,.13)}
.request-card p{position:absolute;left:17px;font-size:5.8px;color:var(--ink)}
.request-card .field{position:absolute;height:16px}
.request-card .btn{position:absolute;left:17px;top:99px;width:81px;height:18px;margin:0}
</style>
</head>
<body>
<div class="stage">

<!-- ============ PAGE: dictionary ============ -->
<section class="page page--dictionary">
  <header class="site-header">
    <div class="brand"><span class="brand-dot"></span><span class="brand-name">SignQuiverly</span></div>
    <div class="tagline"><strong>LEARN ASL THROUGH VIDEO LESSONS ONLINE</strong><span>You are currently logged in as: <em>mlearner</em></span></div>
  </header>
  <nav class="main-nav"><a>Dashboard</a><a>Lessons<i class="caret"></i></a><a>Lesson List</a><a>Dictionary</a><a>Handshapes<i class="caret"></i></a><a>Locations<i class="caret"></i></a><a>Update Account<i class="caret"></i></a><a>Logout</a></nav>

  <h1 class="page-title">ASL Dictionary</h1>
  <div class="search" style="top:121px"><label>Search the dictionary:</label><div class="field">Enter Key Word</div><div class="btn">SEARCH</div></div>
  <div class="alphabet" style="top:164px"><span class="is-current">A</span><span>B</span><span>C</span><span>D</span><span>E</span><span>F</span><span>G</span><span>H</span><span>I</span><span>J</span><span>K</span><span>L</span><span>M</span><span>N</span><span>O</span><span>P</span><span>Q</span><span>R</span><span>S</span><span>T</span><span>U</span><span>V</span><span>W</span><span>X</span><span>Y</span><span>Z</span></div>

  <ul class="word-list col-1"><li>ABC Letter</li><li>ASL 1</li><li>ASL Interpreter</li><li>ATM</li><li>ATM machine</li><li>Abandon</li><li>Abate</li><li>Abdomen</li><li>Abhor</li><li>Abhorrence</li><li>Abide</li><li>Ability</li><li>A bit</li><li>Ablaze</li><li>Able</li><li>Abomination</li><li>About</li><li>About-face</li><li>Above</li><li>Abram Linwood</li><li>Abrupt</li><li>Abruptly</li><li>Absence</li><li>Absolutely</li><li>Absolve</li><li>Abstain</li><li>Abuse</li><li>Abysmal</li><li>Academic</li><li>Academy</li><li>Accelerator</li><li>Accept</li><li>Access</li><li>Accessories</li><li>Privacy - Te</li><li>Accident</li><li>Accidentally</li><li>Accommodate</li><li>Accommodation</li><li>Accompany</li><li>Accomplish</li><li>Accomplishment</li><li>Accord</li><li>According (to)</li><li>Account</li><li>Accountability</li><li>Accountant</li><li>Accounting</li><li>Accumulate</li><li>Accurate</li><li>Accusation</li><li>Accuse</li><li>Accustomed</li><li>Ache</li><li>Achieve</li><li>Achievement</li><li>Achieves</li><li>Acknowledge</li><li>Acquaintance</li><li>Acquire</li><li>Acquisition</li><li>Acre</li><li>Acrobatics</li><li>Across</li><li>Act</li><li>Action</li><li>Actions</li><li>Activate</li><li>Active</li><li>Activist</li><li>Activities</li><li>Activity</li><li>Actual</li><li>Actually</li><li>Adapt</li><li>Add</li><li>Added</li><li>Addendum</li><li>Addict</li><li>Addiction</li><li>Addition</li><li>Additional</li><li>Additionally</li><li>Address</li><li>Address (phys)</li><li>Adequate</li><li>Adhere</li><li>Adhesive</li><li>Adjacent to</li><li>Adjust</li><li>Administration</li><li>Administrative</li></ul>
  <ul class="word-list col-2"><li>Administrator</li><li>Admiration</li><li>Admire</li><li>Admirer</li><li>Admissions</li><li>Admit</li><li>Adolescence</li><li>Adolescent</li><li>Adopt</li><li>Adopted</li><li>Adoption Papers</li><li>Adorables</li><li>Adoration</li><li>Adore</li><li>Adrenaline</li><li>Ads</li><li>Adult</li><li>Advance</li><li>Advancing</li><li>Advantage</li><li>Adventure</li><li>Adverb</li><li>Adversary</li><li>Adversity</li><li>Advertisement</li><li>Advice</li><li>Advocate</li><li>Afar</li><li>Affect</li><li>Affection</li><li>Affection</li><li>Affectionate</li><li>Affidavit</li><li>Affiliation</li><li>Affirmation</li><li>Affect</li><li>Affliction</li><li>Afflicted</li><li>Affluent</li><li>Aficionado</li><li>Afraid</li><li>Africa</li><li>After</li><li>Afternoon</li><li>After that</li><li>Again</li><li>Again and again</li><li>Agape</li><li>Age</li><li>Aged</li><li>Agency</li><li>Agent</li><li>Aggressive</li><li>Aghast</li><li>Agitate</li><li>Agitated</li><li>Ago</li><li>Agonize</li><li>Agony</li><li>A great Deal</li><li>Agree</li><li>Agreeable</li><li>Agreement</li><li>Ahead</li><li>Ahead Of</li><li>Ahead of Time</li><li>Aid</li><li>Ailing</li><li>Ailment</li><li>Aim</li><li>Air</li><li>Air bag</li><li>Airbag</li><li>Aircraft</li><li>Airplane</li><li>Airport</li><li>Airs</li><li>Aisle</li><li>Ajar</li><li>Akin</li><li>Alarm</li><li>Alaska</li><li>Album</li><li>Alcohol</li><li>Alcoholism</li><li>Alert</li><li>Algebra</li><li>Alien</li><li>Alike</li><li>A Little bit</li><li>All</li><li>All American</li></ul>
  <ul class="word-list col-3"><li>All around</li><li>Allegation</li><li>Allegiance</li><li>Allergic</li><li>Allergies</li><li>Allergy</li><li>Alleviate</li><li>All heart</li><li>Alligator</li><li>All in</li><li>All of us</li><li>All of you</li><li>Allotment</li><li>All over</li><li>Allow</li><li>All purpose flour</li><li>Ally</li><li>All year</li><li>Almost</li><li>Aloe</li><li>Alone</li><li>Along</li><li>Alongside</li><li>A long time ago</li><li>Along with</li><li>Aloof</li><li>A lot</li><li>Alot</li><li>Alpaca</li><li>Alphabet B</li><li>Alphabet C</li><li>Alphabet D</li><li>Alphabet E</li><li>Alphabet F</li><li>Alphabet G</li><li>Alphabet H</li><li>Alphabet I</li><li>Alphabet J</li><li>Alphabet K</li><li>Alphabet M</li><li>Alphabet o</li><li>Alphabet P</li><li>Alphabet Q</li><li>Alphabet R</li><li>Alphabet U</li><li>Alphabet v</li><li>Alphabet W</li><li>Alphabet X</li><li>Alphabet Y</li><li>Alphabet z</li><li>Already</li><li>Alright</li><li>Also</li><li>Alter</li><li>Alteration</li><li>Alternative</li><li>Although</li><li>Alto</li><li>Alumni</li><li>Always</li><li>Alzheimer's</li><li>Am</li><li>Amateurish</li><li>Amazed</li><li>Amazing</li><li>Amazon River</li><li>Ambiguity</li><li>Amble</li><li>Amendment</li><li>America</li><li>American</li><li>Amish</li><li>A mixture of</li><li>A moment ago</li><li>Amount</li><li>Ample</li><li>Amputate</li><li>Amsterdam</li><li>Amuse</li><li>Amusement</li><li>Amusing</li><li>An</li><li>Anaerobic</li><li>Analysis</li><li>Analyze</li><li>Anatomy</li><li>Anchor</li><li>Anchorperson</li><li>Ancient</li><li>Ancillary</li><li>And</li><li>Andy</li></ul>
  <ul class="word-list col-4"><li>Anecdote</li><li>Angel</li><li>Angela</li><li>Angry</li><li>Anguish</li><li>Animal</li><li>Animation</li><li>Anime</li><li>Animosity</li><li>Ankle</li><li>Annihilate</li><li>Anniversary</li><li>Announce</li><li>Announcement</li><li>Annoyance</li><li>Annoyed</li><li>Annual</li><li>Anoint</li><li>Anonymity</li><li>Anonymous</li><li>Another</li><li>Answer</li><li>Answers</li><li>Ant</li><li>Antagonism</li><li>Antagonist</li><li>Antarctica</li><li>Anthony</li><li>Anthropology</li><li>Anticipate</li><li>Antipsychotic</li><li>Anxiety</li><li>Anxious</li><li>Any</li><li>Anybody</li><li>Anyhow</li><li>Anymore</li><li>Anyone</li><li>Any Person</li><li>Anyplace</li><li>Anything</li><li>Anyway</li><li>Anywhere</li><li>Apart</li><li>Apartment</li><li>Apathetic</li><li>Ape</li><li>Apocalypse</li><li>Apologetic</li><li>Apostrophe</li><li>App</li><li>Appaling</li><li>Appalled</li><li>Apparatus</li><li>Apparent</li><li>Apparently</li><li>Appealing</li><li>Appear</li><li>Appearance</li><li>Appease</li><li>Append</li><li>Appendage</li><li>Appetite</li><li>Appetizing</li><li>Applaud</li><li>Applause</li><li>Apple</li><li>Apple Orchard</li><li>Apple Sauce</li><li>Appliances</li><li>Applicant</li><li>Application</li><li>Appoint</li><li>Appointment</li><li>Appreciate</li><li>Apprehend</li><li>Apprehension</li><li>Apprehensive</li><li>Apprentice</li><li>Apprentice</li><li>Apprise</li><li>Approach</li><li>Appropriate</li><li>Approval</li><li>Approve</li><li>Approximation</li><li>Apricot</li><li>April</li><li>Aptitude</li><li>Aquarium</li><li>Aquarius</li><li>Aquire</li></ul>
  <ul class="word-list col-5"><li>Arab</li><li>Arabic</li><li>Arbitrary</li><li>Architect</li><li>Are</li><li>Area</li><li>Arena</li><li>Argentina</li><li>Argue</li><li>Arguing</li><li>Argument</li><li>Aria Granton</li><li>Arise</li><li>Aristocratic</li><li>Arithmetic</li><li>Arizona</li><li>Arlington</li><li>Arm</li><li>Armchair</li><li>Armed Forces</li><li>Armenian</li><li>Armlet</li><li>Army</li><li>Aroma</li><li>Around</li><li>Arraignment</li><li>Arrange</li><li>Arrangement</li><li>Array</li><li>Arrest</li><li>Arrested</li><li>Arrival</li><li>Arrive</li><li>Arrogance</li><li>Arrogant</li><li>Arrow</li><li>Arson</li><li>Art</li><li>Artichoke</li><li>Article</li><li>Articulate</li><li>Artist</li><li>Artistic</li><li>Art museum</li><li>Artwork</li><li>As</li><li>Ash</li><li>Ashamed</li><li>Ashen</li><li>Asia</li><li>Aside</li><li>Ask</li><li>Asked</li><li>Askew</li><li>Asking price</li><li>Ask slow down and again</li><li>As of now</li><li>As opposed to</li><li>Aspect</li><li>Asphyxiate</li><li>Aspiration</li><li>Aspire</li><li>Aspire</li><li>Assassinate</li><li>Assault</li><li>Assault and battery</li><li>Assemble</li><li>Assembly</li><li>Assembly person</li><li>Assessment</li><li>Assignment</li><li>Assignment</li><li>Assignment on time</li><li>Assist</li><li>Assistant</li><li>Assistant apply</li><li>Assistant principal</li><li>Associate</li><li>Associate principal</li><li>Association</li><li>Assorted</li><li>Assortment</li><li>Assume</li><li>Assurance</li><li>Assure</li><li>Asthma</li><li>Astonishing</li><li>Astounding</li><li>Astronaut</li><li>Astronomy</li><li>As well</li></ul>
  <ul class="word-list col-6"><li>As well as</li><li>Asylum</li><li>At</li><li>At any rate</li><li>Ate</li><li>At fault</li><li>Atheist</li><li>Athlete</li><li>Athletic</li><li>Atlanta</li><li>At last</li><li>Atmosphere</li><li>Atom</li><li>At one time</li><li>Atrocity</li><li>Attach</li><li>Attache case</li><li>Attachment</li><li>Attachment</li><li>Attack</li><li>Attain</li><li>Attained</li><li>Attempt</li><li>Attend</li><li>Attendance</li><li>Attention</li><li>Attentive</li><li>At the back</li><li>At the rear</li><li>Attic</li><li>At times</li><li>Attire</li><li>Attitude</li><li>Attorney</li><li>Attraction</li><li>Attractions</li><li>Attractive</li><li>Attributes</li><li>Auction</li><li>Audacious</li><li>Audacity</li><li>Audience</li><li>Audio</li><li>Audiologist</li><li>Audism</li><li>Audition</li><li>Auditorium</li><li>August</li><li>Aunt</li><li>Au pair</li><li>Austin</li><li>Australia</li><li>Authentic</li><li>Author</li><li>Authored</li><li>Authoritarianism</li><li>Authority</li><li>Autism</li><li>Autistic</li><li>Auto</li><li>Autocracy</li><li>Autograph</li><li>Automobile</li><li>Automobile</li><li>Autonomous</li><li>Autumn</li><li>Auxiliary</li><li>Available</li><li>Aventures</li><li>Avenue</li><li>Average</li><li>Aversion</li><li>Avoid</li><li>Awake</li><li>Awaken</li><li>Award</li><li>Aware</li><li>Awareness</li><li>Awe inspiring</li><li>Awesome</li><li>Awful</li><li>Awkward</li><li>Ax</li><li>Axe</li><li>A year Ago</li><li>A year now</li><li>age old</li><li>Archaic</li></ul>

  <div class="alphabet" style="top:1391px"><span class="is-current">A</span><span>B</span><span>C</span><span>D</span><span>E</span><span>F</span><span>G</span><span>H</span><span>I</span><span>J</span><span>K</span><span>L</span><span>M</span><span>N</span><span>O</span><span>P</span><span>Q</span><span>R</span><span>S</span><span>T</span><span>U</span><span>V</span><span>W</span><span>X</span><span>Y</span><span>Z</span></div>

  <footer class="site-footer">
    <div class="foot-brand"><span class="brand-dot"></span><span class="brand-name">SignQuiverly</span></div>
    <p class="foot-about">SignQuiverly is a subscription based website for American Sign Language (ASL) video lessons. The content is for anyone who wishes to learn ASL, regardless of age. It has been designed to instruct Deaf students, parents of Deaf children, and the community-at-large. You may cancel your subscription at any time. All lessons are taught by Deaf experts of ASL.</p>
    <span class="foot-divider" style="left:175px"></span>
    <h3 class="foot-head" style="left:192px">Quick Links</h3>
    <ul class="foot-links" style="left:192px"><li>Home</li><li>Try it Free</li><li>Contact Us</li></ul>
    <ul class="foot-links" style="left:266px"><li>Group Rate Form</li><li>Teacher's Guide</li><li>Gift Certificates</li><li>FAQs</li><li>Privacy Policy</li></ul>
    <span class="foot-divider" style="left:342px"></span>
    <h3 class="foot-head" style="left:355px">Contact Us</h3>
    <ul class="contact">
      <li><svg viewBox="0 0 10 10"><path d="M5 0a3.6 3.6 0 0 0-3.6 3.6C1.4 6.3 5 10 5 10s3.6-3.7 3.6-6.4A3.6 3.6 0 0 0 5 0zm0 5a1.4 1.4 0 1 1 0-2.8A1.4 1.4 0 0 1 5 5z"/></svg>PO Box 55012, Maple Ridge, MI 48000</li>
      <li><svg viewBox="0 0 10 10"><path d="M2 0l2 2.5-1 1.3a6 6 0 0 0 3.2 3.2l1.3-1L10 8l-1.2 1.6C4.5 10 0 5.5.4 1.2z"/></svg>(555) 014-2280</li>
      <li><svg viewBox="0 0 10 10"><path d="M0 1.5h10v7H0zm1 1l4 3 4-3"/></svg>info@signquiverly.com</li>
    </ul>
    <div class="foot-rule"></div>
    <p class="copyright">Copyrights © 2021, SignQuiverly. All rights reserved. Terms &amp; Conditions</p>
    <div class="social"><span></span><span></span><span></span><span></span><span></span></div>
  </footer>
</section>

<!-- ============ PAGE: dictionary with video modal ============ -->
<section class="page page--modal">
  <header class="site-header">
    <div class="brand"><span class="brand-dot"></span><span class="brand-name">SignQuiverly</span></div>
    <div class="tagline"><strong>LEARN ASL THROUGH VIDEO LESSONS ONLINE</strong><span>You are currently logged in as: <em>mlearner</em></span></div>
  </header>
  <nav class="main-nav"><a>Dashboard</a><a>Lessons<i class="caret"></i></a><a>Lesson List</a><a>Dictionary</a><a>Handshapes<i class="caret"></i></a><a>Locations<i class="caret"></i></a><a>Update Account<i class="caret"></i></a><a>Logout</a></nav>

  <h1 class="page-title">ASL Dictionary</h1>
  <div class="search" style="top:121px"><label>Search the dictionary:</label><div class="field">Enter Key Word</div><div class="btn">SEARCH</div></div>
  <div class="alphabet" style="top:164px"><span class="is-current">A</span><span>B</span><span>C</span><span>D</span><span>E</span><span>F</span><span>G</span><span>H</span><span>I</span><span>J</span><span>K</span><span>L</span><span>M</span><span>N</span><span>O</span><span>P</span><span>Q</span><span>R</span><span>S</span><span>T</span><span>U</span><span>V</span><span>W</span><span>X</span><span>Y</span><span>Z</span></div>

  <ul class="word-list col-1"><li>ABC Letter</li><li>ASL 1</li><li>ASL Interpreter</li><li>ATM</li><li>ATM machine</li><li>Abandon</li><li>Abate</li><li>Abdomen</li><li>Abhor</li><li>Abhorrence</li><li>Abide</li><li>Ability</li><li>A bit</li><li>Ablaze</li><li>Able</li><li>Abomination</li><li>About</li><li>About-face</li><li>Above</li><li>Abram Linwood</li><li>Abrupt</li><li>Abruptly</li><li>Absence</li><li>Absolutely</li><li>Absolve</li><li>Abstain</li><li>Abuse</li><li>Abysmal</li><li>Academic</li><li>Academy</li><li>Accelerator</li><li>Accept</li><li>Access</li><li>Accessories</li><li>Privacy - Te</li><li>Accident</li><li>Accidentally</li><li>Accommodate</li><li>Accommodation</li><li>Accompany</li><li>Accomplish</li><li>Accomplishment</li><li>Accord</li><li>According (to)</li><li>Account</li><li>Accountability</li><li>Accountant</li><li>Accounting</li><li>Accumulate</li><li>Accurate</li><li>Accusation</li><li>Accuse</li><li>Accustomed</li><li>Ache</li><li>Achieve</li><li>Achievement</li><li>Achieves</li><li>Acknowledge</li><li>Acquaintance</li><li>Acquire</li><li>Acquisition</li><li>Acre</li><li>Acrobatics</li><li>Across</li><li>Act</li><li>Action</li><li>Actions</li><li>Activate</li><li>Active</li><li>Activist</li><li>Activities</li><li>Activity</li><li>Actual</li><li>Actually</li><li>Adapt</li><li>Add</li><li>Added</li><li>Addendum</li><li>Addict</li><li>Addiction</li><li>Addition</li><li>Additional</li><li>Additionally</li><li>Address</li><li>Address (phys)</li><li>Adequate</li><li>Adhere</li><li>Adhesive</li><li>Adjacent to</li><li>Adjust</li><li>Administration</li><li>Administrative</li></ul>
  <ul class="word-list col-2"><li>Administrator</li><li>Admiration</li><li style="color:#e08a2c">Admire</li><li>Admirer</li><li>Admissions</li><li>Admit</li><li>Adolescence</li><li>Adolescent</li><li>Adopt</li><li>Adopted</li><li>Adoption Papers</li><li>Adorables</li><li>Adoration</li><li>Adore</li><li>Adrenaline</li><li>Ads</li><li>Adult</li><li>Advance</li><li>Advancing</li><li>Advantage</li><li>Adventure</li><li>Adverb</li><li>Adversary</li><li>Adversity</li><li>Advertisement</li><li>Advice</li><li>Advocate</li><li>Afar</li><li>Affect</li><li>Affection</li><li>Affection</li><li>Affectionate</li><li>Affidavit</li><li>Affiliation</li><li>Affirmation</li><li>Affect</li><li>Affliction</li><li>Afflicted</li><li>Affluent</li><li>Aficionado</li><li>Afraid</li><li>Africa</li><li>After</li><li>Afternoon</li><li>After that</li><li>Again</li><li>Again and again</li><li>Agape</li><li>Age</li><li>Aged</li><li>Agency</li><li>Agent</li><li>Aggressive</li><li>Aghast</li><li>Agitate</li><li>Agitated</li><li>Ago</li><li>Agonize</li><li>Agony</li><li>A great Deal</li><li>Agree</li><li>Agreeable</li><li>Agreement</li><li>Ahead</li><li>Ahead Of</li><li>Ahead of Time</li><li>Aid</li><li>Ailing</li><li>Ailment</li><li>Aim</li><li>Air</li><li>Air bag</li><li>Airbag</li><li>Aircraft</li><li>Airplane</li><li>Airport</li><li>Airs</li><li>Aisle</li><li>Ajar</li><li>Akin</li><li>Alarm</li><li>Alaska</li><li>Album</li><li>Alcohol</li><li>Alcoholism</li><li>Alert</li><li>Algebra</li><li>Alien</li><li>Alike</li><li>A Little bit</li><li>All</li><li>All American</li></ul>
  <ul class="word-list col-3"><li>All around</li><li>Allegation</li><li>Allegiance</li><li>Allergic</li><li>Allergies</li><li>Allergy</li><li>Alleviate</li><li>All heart</li><li>Alligator</li><li>All in</li><li>All of us</li><li>All of you</li><li>Allotment</li><li>All over</li><li>Allow</li><li>All purpose flour</li><li>Ally</li><li>All year</li><li>Almost</li><li>Aloe</li><li>Alone</li><li>Along</li><li>Alongside</li><li>A long time ago</li><li>Along with</li><li>Aloof</li><li>A lot</li><li>Alot</li><li>Alpaca</li><li>Alphabet B</li><li>Alphabet C</li><li>Alphabet D</li><li>Alphabet E</li><li>Alphabet F</li><li>Alphabet G</li><li>Alphabet H</li><li>Alphabet I</li><li>Alphabet J</li><li>Alphabet K</li><li>Alphabet M</li><li>Alphabet o</li><li>Alphabet P</li><li>Alphabet Q</li><li>Alphabet R</li><li>Alphabet U</li><li>Alphabet v</li><li>Alphabet W</li><li>Alphabet X</li><li>Alphabet Y</li><li>Alphabet z</li><li>Already</li><li>Alright</li><li>Also</li><li>Alter</li><li>Alteration</li><li>Alternative</li><li>Although</li><li>Alto</li><li>Alumni</li><li>Always</li><li>Alzheimer's</li><li>Am</li><li>Amateurish</li><li>Amazed</li><li>Amazing</li><li>Amazon River</li><li>Ambiguity</li><li>Amble</li><li>Amendment</li><li>America</li><li>American</li><li>Amish</li><li>A mixture of</li><li>A moment ago</li><li>Amount</li><li>Ample</li><li>Amputate</li><li>Amsterdam</li><li>Amuse</li><li>Amusement</li><li>Amusing</li><li>An</li><li>Anaerobic</li><li>Analysis</li><li>Analyze</li><li>Anatomy</li><li>Anchor</li><li>Anchorperson</li><li>Ancient</li><li>Ancillary</li><li>And</li><li>Andy</li></ul>
  <ul class="word-list col-4"><li>Anecdote</li><li>Angel</li><li>Angela</li><li>Angry</li><li>Anguish</li><li>Animal</li><li>Animation</li><li>Anime</li><li>Animosity</li><li>Ankle</li><li>Annihilate</li><li>Anniversary</li><li>Announce</li><li>Announcement</li><li>Annoyance</li><li>Annoyed</li><li>Annual</li><li>Anoint</li><li>Anonymity</li><li>Anonymous</li><li>Another</li><li>Answer</li><li>Answers</li><li>Ant</li><li>Antagonism</li><li>Antagonist</li><li>Antarctica</li><li>Anthony</li><li>Anthropology</li><li>Anticipate</li><li>Antipsychotic</li><li>Anxiety</li><li>Anxious</li><li>Any</li><li>Anybody</li><li>Anyhow</li><li>Anymore</li><li>Anyone</li><li>Any Person</li><li>Anyplace</li><li>Anything</li><li>Anyway</li><li>Anywhere</li><li>Apart</li><li>Apartment</li><li>Apathetic</li><li>Ape</li><li>Apocalypse</li><li>Apologetic</li><li>Apostrophe</li><li>App</li><li>Appaling</li><li>Appalled</li><li>Apparatus</li><li>Apparent</li><li>Apparently</li><li>Appealing</li><li>Appear</li><li>Appearance</li><li>Appease</li><li>Append</li><li>Appendage</li><li>Appetite</li><li>Appetizing</li><li>Applaud</li><li>Applause</li><li>Apple</li><li>Apple Orchard</li><li>Apple Sauce</li><li>Appliances</li><li>Applicant</li><li>Application</li><li>Appoint</li><li>Appointment</li><li>Appreciate</li><li>Apprehend</li><li>Apprehension</li><li>Apprehensive</li><li>Apprentice</li><li>Apprentice</li><li>Apprise</li><li>Approach</li><li>Appropriate</li><li>Approval</li><li>Approve</li><li>Approximation</li><li>Apricot</li><li>April</li><li>Aptitude</li><li>Aquarium</li><li>Aquarius</li><li>Aquire</li></ul>
  <ul class="word-list col-5"><li>Arab</li><li>Arabic</li><li>Arbitrary</li><li>Architect</li><li>Are</li><li>Area</li><li>Arena</li><li>Argentina</li><li>Argue</li><li>Arguing</li><li>Argument</li><li>Aria Granton</li><li>Arise</li><li>Aristocratic</li><li>Arithmetic</li><li>Arizona</li><li>Arlington</li><li>Arm</li><li>Armchair</li><li>Armed Forces</li><li>Armenian</li><li>Armlet</li><li>Army</li><li>Aroma</li><li>Around</li><li>Arraignment</li><li>Arrange</li><li>Arrangement</li><li>Array</li><li>Arrest</li><li>Arrested</li><li>Arrival</li><li>Arrive</li><li>Arrogance</li><li>Arrogant</li><li>Arrow</li><li>Arson</li><li>Art</li><li>Artichoke</li><li>Article</li><li>Articulate</li><li>Artist</li><li>Artistic</li><li>Art museum</li><li>Artwork</li><li>As</li><li>Ash</li><li>Ashamed</li><li>Ashen</li><li>Asia</li><li>Aside</li><li>Ask</li><li>Asked</li><li>Askew</li><li>Asking price</li><li>Ask slow down and again</li><li>As of now</li><li>As opposed to</li><li>Aspect</li><li>Asphyxiate</li><li>Aspiration</li><li>Aspire</li><li>Aspire</li><li>Assassinate</li><li>Assault</li><li>Assault and battery</li><li>Assemble</li><li>Assembly</li><li>Assembly person</li><li>Assessment</li><li>Assignment</li><li>Assignment</li><li>Assignment on time</li><li>Assist</li><li>Assistant</li><li>Assistant apply</li><li>Assistant principal</li><li>Associate</li><li>Associate principal</li><li>Association</li><li>Assorted</li><li>Assortment</li><li>Assume</li><li>Assurance</li><li>Assure</li><li>Asthma</li><li>Astonishing</li><li>Astounding</li><li>Astronaut</li><li>Astronomy</li><li>As well</li></ul>
  <ul class="word-list col-6"><li>As well as</li><li>Asylum</li><li>At</li><li>At any rate</li><li>Ate</li><li>At fault</li><li>Atheist</li><li>Athlete</li><li>Athletic</li><li>Atlanta</li><li>At last</li><li>Atmosphere</li><li>Atom</li><li>At one time</li><li>Atrocity</li><li>Attach</li><li>Attache case</li><li>Attachment</li><li>Attachment</li><li>Attack</li><li>Attain</li><li>Attained</li><li>Attempt</li><li>Attend</li><li>Attendance</li><li>Attention</li><li>Attentive</li><li>At the back</li><li>At the rear</li><li>Attic</li><li>At times</li><li>Attire</li><li>Attitude</li><li>Attorney</li><li>Attraction</li><li>Attractions</li><li>Attractive</li><li>Attributes</li><li>Auction</li><li>Audacious</li><li>Audacity</li><li>Audience</li><li>Audio</li><li>Audiologist</li><li>Audism</li><li>Audition</li><li>Auditorium</li><li>August</li><li>Aunt</li><li>Au pair</li><li>Austin</li><li>Australia</li><li>Authentic</li><li>Author</li><li>Authored</li><li>Authoritarianism</li><li>Authority</li><li>Autism</li><li>Autistic</li><li>Auto</li><li>Autocracy</li><li>Autograph</li><li>Automobile</li><li>Automobile</li><li>Autonomous</li><li>Autumn</li><li>Auxiliary</li><li>Available</li><li>Aventures</li><li>Avenue</li><li>Average</li><li>Aversion</li><li>Avoid</li><li>Awake</li><li>Awaken</li><li>Award</li><li>Aware</li><li>Awareness</li><li>Awe inspiring</li><li>Awesome</li><li>Awful</li><li>Awkward</li><li>Ax</li><li>Axe</li><li>A year Ago</li><li>A year now</li><li>age old</li><li>Archaic</li></ul>

  <div class="alphabet" style="top:1391px"><span class="is-current">A</span><span>B</span><span>C</span><span>D</span><span>E</span><span>F</span><span>G</span><span>H</span><span>I</span><span>J</span><span>K</span><span>L</span><span>M</span><span>N</span><span>O</span><span>P</span><span>Q</span><span>R</span><span>S</span><span>T</span><span>U</span><span>V</span><span>W</span><span>X</span><span>Y</span><span>Z</span></div>

  <footer class="site-footer">
    <div class="foot-brand"><span class="brand-dot"></span><span class="brand-name">SignQuiverly</span></div>
    <p class="foot-about">SignQuiverly is a subscription based website for American Sign Language (ASL) video lessons. The content is for anyone who wishes to learn ASL, regardless of age. It has been designed to instruct Deaf students, parents of Deaf children, and the community-at-large. You may cancel your subscription at any time. All lessons are taught by Deaf experts of ASL.</p>
    <span class="foot-divider" style="left:175px"></span>
    <h3 class="foot-head" style="left:192px">Quick Links</h3>
    <ul class="foot-links" style="left:192px"><li>Home</li><li>Try it Free</li><li>Contact Us</li></ul>
    <ul class="foot-links" style="left:266px"><li>Group Rate Form</li><li>Teacher's Guide</li><li>Gift Certificates</li><li>FAQs</li><li>Privacy Policy</li></ul>
    <span class="foot-divider" style="left:342px"></span>
    <h3 class="foot-head" style="left:355px">Contact Us</h3>
    <ul class="contact">
      <li><svg viewBox="0 0 10 10"><path d="M5 0a3.6 3.6 0 0 0-3.6 3.6C1.4 6.3 5 10 5 10s3.6-3.7 3.6-6.4A3.6 3.6 0 0 0 5 0zm0 5a1.4 1.4 0 1 1 0-2.8A1.4 1.4 0 0 1 5 5z"/></svg>PO Box 55012, Maple Ridge, MI 48000</li>
      <li><svg viewBox="0 0 10 10"><path d="M2 0l2 2.5-1 1.3a6 6 0 0 0 3.2 3.2l1.3-1L10 8l-1.2 1.6C4.5 10 0 5.5.4 1.2z"/></svg>(555) 014-2280</li>
      <li><svg viewBox="0 0 10 10"><path d="M0 1.5h10v7H0zm1 1l4 3 4-3"/></svg>info@signquiverly.com</li>
    </ul>
    <div class="foot-rule"></div>
    <p class="copyright">Copyrights © 2021, SignQuiverly. All rights reserved. Terms &amp; Conditions</p>
    <div class="social"><span></span><span></span><span></span><span></span><span></span></div>
  </footer>

  <div class="shade"></div>
  <div class="vocab-modal">
    <div class="modal-bar">
      <svg class="plus" viewBox="0 0 10 10"><circle cx="5" cy="5" r="4.3" fill="none" stroke="#fff" stroke-width="1.3"/><path d="M5 2.6v4.8M2.6 5h4.8" stroke="#fff" stroke-width="1.3"/></svg>
      <u>Add to My Vocabulary</u><span class="modal-close"></span>
    </div>
    <div class="video" role="img" aria-label="Video of a Deaf instructor signing the word Admire against a green backdrop">
      <div class="slow-toggle"><i></i>Slow video playback</div>
      <div class="video-controls"><b></b><span>0:00 / 0:04</span><em></em><span>◂)</span><span>⋮</span></div>
    </div>
    <p class="term" style="top:157px"><strong>Term:</strong> <span class="blue">Admire</span></p>
    <p class="term" style="top:167px"><strong>Synonyms:</strong> <span class="red">Marvel at, Think highly of, High regard for</span></p>
    <p class="term" style="top:178px"><strong>Variations:</strong></p>
  </div>
</section>

<!-- ============ PAGE: dictionary search ============ -->
<section class="page page--search">
  <header class="site-header">
    <div class="brand"><span class="brand-dot"></span><span class="brand-name">SignQuiverly</span></div>
    <div class="tagline"><strong>LEARN ASL THROUGH VIDEO LESSONS ONLINE</strong><span>You are currently logged in as: <em>mlearner</em></span></div>
  </header>
  <nav class="main-nav"><a>Dashboard</a><a>Lessons<i class="caret"></i></a><a>Lesson List</a><a>Dictionary</a><a>Handshapes<i class="caret"></i></a><a>Locations<i class="caret"></i></a><a>Update Account<i class="caret"></i></a><a>Logout</a></nav>

  <h1 class="page-title">Dictionary Search</h1>
  <p class="page-sub">We've searched our dictionary, and here's what we've come up with:</p>
  <div class="search" style="top:137px"><label>Search the dictionary:</label><div class="field">Admire</div><div class="btn">SEARCH</div></div>
  <div class="results">
    <span class="hit" style="left:48px">Admire</span>
    <span class="hit" style="left:104px">Admire</span>
    <span style="left:160px">High regard for</span>
    <span style="left:237px">Marvel at</span>
    <span style="left:299px">Think highly of</span>
  </div>

  <div class="request-card">
    <p style="top:16px">Can't find the word you're looking for ? Use the form below to request that we we add it to our dictionary</p>
    <p style="top:36px">Word to add:</p>
    <div class="field" style="left:59px;top:32px;width:138px">Admire</div>
    <p style="top:57px">Sample sentence or definition of the word to give us context so we can properly sign your word.</p>
    <div class="field" style="left:17px;top:77px;width:137px">Admire</div>
    <div class="btn">REQUEST WORD</div>
  </div>

  <footer class="site-footer">
    <div class="foot-brand"><span class="brand-dot"></span><span class="brand-name">SignQuiverly</span></div>
    <p class="foot-about">SignQuiverly is a subscription based website for American Sign Language (ASL) video lessons. The content is for anyone who wishes to learn ASL, regardless of age. It has been designed to instruct Deaf students, parents of Deaf children, and the community-at-large. You may cancel your subscription at any time. All lessons are taught by Deaf experts of ASL.</p>
    <span class="foot-divider" style="left:175px"></span>
    <h3 class="foot-head" style="left:192px">Quick Links</h3>
    <ul class="foot-links" style="left:192px"><li>Home</li><li>Try it Free</li><li>Contact Us</li></ul>
    <ul class="foot-links" style="left:266px"><li>Group Rate Form</li><li>Teacher's Guide</li><li>Gift Certificates</li><li>FAQs</li><li>Privacy Policy</li></ul>
    <span class="foot-divider" style="left:342px"></span>
    <h3 class="foot-head" style="left:355px">Contact Us</h3>
    <ul class="contact">
      <li><svg viewBox="0 0 10 10"><path d="M5 0a3.6 3.6 0 0 0-3.6 3.6C1.4 6.3 5 10 5 10s3.6-3.7 3.6-6.4A3.6 3.6 0 0 0 5 0zm0 5a1.4 1.4 0 1 1 0-2.8A1.4 1.4 0 0 1 5 5z"/></svg>PO Box 55012, Maple Ridge, MI 48000</li>
      <li><svg viewBox="0 0 10 10"><path d="M2 0l2 2.5-1 1.3a6 6 0 0 0 3.2 3.2l1.3-1L10 8l-1.2 1.6C4.5 10 0 5.5.4 1.2z"/></svg>(555) 014-2280</li>
      <li><svg viewBox="0 0 10 10"><path d="M0 1.5h10v7H0zm1 1l4 3 4-3"/></svg>info@signquiverly.com</li>
    </ul>
    <div class="foot-rule"></div>
    <p class="copyright">Copyrights © 2021, SignQuiverly. All rights reserved. Terms &amp; Conditions</p>
    <div class="social"><span></span><span></span><span></span><span></span><span></span></div>
  </footer>
</section>

</div>
</body>
</html>
```